Meridian Callware business card design

I would like to see some designs for a business card for Meridian Callware. I would like the business card to be double sided. It will need to have a similar colour / look and feel to our website www.meridiancallware.com.au I have also attached our latest flyer. Final designs to be handed over in Photoshop format so that I can edit the business card when needed please.

Industry/Entity Type

Business

Contact Information for Business Card

Kelvin Ashworth
sales@meridiancallware.com.au
Business Development Manager
ph: (08) 6517 2984
www.meridiancallware.com.au

Font styles to use
Serif
Sans Serif

Requirements
Must have
• If you could please utilise our colour scheme as seen on our website and the attached flyer.
• I would also like the final design to be in a Photoshop format so that I can edit it when needed please.

```html
<!DOCTYPE html>
<html lang="en">
<head>
<meta charset="utf-8">
<title>Meridian Callware – Business Card</title>
<link rel="stylesheet" href="https://fonts.googleapis.com/css2?family=Open+Sans:wght@400;600&family=Roboto:wght@400&display=swap">
<style>
  :root {
    --backdrop: #3b3330;
    --card-black: #17181a;
    --card-edge: #0d0d0e;
    --gloss-grey: #3a3c40;
    --brand-blue: #1a8fe0;
    --band-blue-dark: #0b5fb0;
    --band-blue-light: #2fa3ec;
    --band-teal: #3ec9a0;
    --text-white: #f2f4f6;
    --text-soft: #c9ced4;
  }
  * { box-sizing: border-box; margin: 0; padding: 0; }
  html, body {
    width: 1200px;
    height: 716px;
    overflow: hidden;
    background: var(--backdrop);
  }
  .canvas {
    position: relative;
    width: 1200px;
    height: 716px;
    display: flex;
    align-items: center;
    justify-content: center;
    gap: 60px;
  }
  .card {
    position: relative;
    width: 520px;
    height: 300px;
    background: var(--card-black);
    border-radius: 4px;
    box-shadow: 0 14px 30px rgba(0,0,0,0.45);
    overflow: hidden;
  }

  /* Back side */
  .card-back {
    display: flex;
    align-items: center;
    justify-content: center;
  }
  .back-wordmark {
    font-family: "Open Sans", sans-serif;
    font-weight: 600;
    font-size: 34px;
    color: var(--gloss-grey);
    letter-spacing: 0.5px;
  }

  /* Front side */
  .wordmark {
    position: absolute;
    left: 30px;
    top: 34px;
    font-family: "Open Sans", sans-serif;
    font-weight: 600;
    font-size: 40px;
    line-height: 1;
    color: var(--text-white);
    letter-spacing: -0.5px;
  }
  .tagline {
    position: absolute;
    left: 34px;
    top: 82px;
    font-family: "Open Sans", sans-serif;
    font-weight: 400;
    font-size: 18px;
    color: var(--text-soft);
  }
  .person {
    position: absolute;
    left: 282px;
    top: 132px;
  }
  .person-name {
    font-family: "Open Sans", sans-serif;
    font-weight: 600;
    font-size: 21px;
    color: var(--brand-blue);
    line-height: 1.1;
  }
  .person-title {
    font-family: "Open Sans", sans-serif;
    font-size: 12px;
    color: var(--text-white);
    margin-top: 2px;
  }
  .contact-list {
    position: absolute;
    left: 258px;
    top: 190px;
    list-style: none;
    font-family: "Roboto", sans-serif;
    font-size: 14px;
    color: var(--text-white);
  }
  .contact-item {
    display: flex;
    align-items: center;
    gap: 10px;
    height: 19px;
  }
  .contact-icon {
    width: 12px;
    height: 12px;
    flex: none;
  }
  .accent-band {
    position: absolute;
    left: 0;
    bottom: 0;
    width: 520px;
    height: 40px;
  }
</style>
</head>
<body>
<main class="canvas">

  <section class="card card-back" aria-label="Business card, back side">
    <span class="back-wordmark">Meridian Callware</span>
  </section>

  <section class="card card-front" aria-label="Business card, front side">
    <div class="wordmark">Meridian Callware</div>
    <div class="tagline">Phone systems for your business</div>

    <div class="person">
      <div class="person-name">Kelvin Ashworth</div>
      <div class="person-title">Business Development Manager</div>
    </div>

    <ul class="contact-list">
      <li class="contact-item">
        <svg class="contact-icon" viewBox="0 0 12 12" aria-hidden="true">
          <path d="M1 4.5 Q6 1 11 4.5 L10 6 L8 5.2 L8 4 Q6 3.3 4 4 L4 5.2 L2 6 Z M3 7 H9 L10 11 H2 Z" fill="var(--brand-blue)"/>
        </svg>
        <span>(08) 6517 2984</span>
      </li>
      <li class="contact-item">
        <svg class="contact-icon" viewBox="0 0 12 12" aria-hidden="true">
          <rect x="0.5" y="2" width="11" height="8" rx="1" fill="var(--brand-blue)"/>
          <path d="M1 2.6 L6 6.6 L11 2.6" fill="none" stroke="var(--card-black)" stroke-width="1"/>
        </svg>
        <span>sales@meridiancallware.com.au</span>
      </li>
      <li class="contact-item">
        <svg class="contact-icon" viewBox="0 0 12 12" aria-hidden="true">
          <circle cx="6" cy="6" r="5.3" fill="var(--brand-blue)"/>
          <g fill="none" stroke="var(--card-black)" stroke-width="0.8">
            <ellipse cx="6" cy="6" rx="2.3" ry="5.3"/>
            <line x1="0.7" y1="6" x2="11.3" y2="6"/>
            <line x1="6" y1="0.7" x2="6" y2="11.3"/>
          </g>
        </svg>
        <span>www.meridiancallware.com.au</span>
      </li>
    </ul>

    <svg class="accent-band" viewBox="0 0 520 40" preserveAspectRatio="none" aria-hidden="true">
      <defs>
        <linearGradient id="bandBlue" x1="0" y1="0" x2="1" y2="0">
          <stop offset="0" stop-color="var(--band-blue-dark)"/>
          <stop offset="1" stop-color="var(--band-blue-light)"/>
        </linearGradient>
      </defs>
      <polygon points="0,0 0,10 520,40 520,30" fill="url(#bandBlue)"/>
      <polygon points="360,30.8 520,40 520,30 380,22" fill="var(--band-teal)"/>
    </svg>
  </section>

</main>
</body>
</html>
```